Book Cover for nonfiction book about defeating one's grief

I need a book cover (front and back) for a book titled Senderos de Sauces (Willow Paths). I have included a word document of the back cover copy. I liked the design of When the river turns (http://www.pixelvarno.com/design/4817302) so something like that would be nice. But if you have a better idea that's fine.
Target Market(s)
People suffering from the loss of a loved one
Requirements
Must have
- Please move the author information (which is the first paragraph) so that it is the last paragraph
- Please include my middle initial in the name (Derek T. Fenwick)
- 6 x 9 inch book, 9mm spine width, 5cm x 3 cm UPC placeholder on back cover
- Thanks!
Nice to have
- should convey relief from grief or some one grieving

```html
<!DOCTYPE html>
<html lang="es">
<head>
<meta charset="utf-8">
<title>Senderos de Sauces — Cubierta</title>
<link rel="stylesheet" href="https://fonts.googleapis.com/css2?family=Great+Vibes&family=Cinzel:wght@400;600&family=Kaushan+Script&family=Arimo:wght@400&display=swap">
<style>
  :root {
    --stage: #e9e6e2;
    --cover-dark: #232120;
    --panel: rgba(28, 26, 25, 0.78);
    --band: rgba(166, 33, 43, 0.92);
    --title-red: #d8232f;
    --ink-light: #ffffff;
    --photo-light: #fbf8f2;
    --photo-mid: #cdb79a;
    --photo-wood: #6b5443;
    --photo-dark: #1f1b19;
    --portrait: #6e6a66;
    --upc: #ffffff;
  }
  html, body {
    margin: 0;
    width: 1200px;
    height: 900px;
    overflow: hidden;
    background: var(--stage);
  }
  .book-cover {
    position: absolute;
    left: 108px;
    top: 105px;
    width: 950px;
    height: 692px;
    background: var(--cover-dark);
    overflow: hidden;
    font-family: "Arimo", Arial, sans-serif;
    color: var(--ink-light);
  }
  .cover-photo {
    position: absolute;
    inset: 0;
    background:
      radial-gradient(ellipse 360px 300px at 76% 30%, var(--photo-light) 0%, var(--photo-light) 35%, var(--photo-mid) 62%, transparent 100%),
      radial-gradient(ellipse 520px 520px at 72% 75%, var(--photo-wood) 0%, rgba(60,46,38,0.7) 55%, transparent 100%),
      linear-gradient(90deg, var(--photo-dark) 0%, var(--photo-dark) 30%, rgba(31,27,25,0) 60%);
  }
  .back-copy {
    position: absolute;
    left: 25px;
    top: 20px;
    width: 412px;
    height: 403px;
    box-sizing: border-box;
    padding: 58px 10px 0 11px;
    background: var(--panel);
    border-radius: 14px;
    font-size: 12.4px;
    line-height: 14.6px;
    text-align: justify;
  }
  .back-copy p { margin: 0; }
  .back-copy p + p.gap { margin-top: 14.6px; }
  .author-band {
    position: absolute;
    left: 0;
    top: 440px;
    width: 100%;
    height: 125px;
    background: var(--band);
  }
  .author-portrait {
    position: absolute;
    left: 25px;
    top: 458px;
    width: 78px;
    height: 90px;
    background: linear-gradient(180deg, #8c8884, var(--portrait));
    border: 1px solid #ddd;
    box-sizing: border-box;
  }
  .author-bio {
    position: absolute;
    left: 110px;
    top: 458px;
    width: 332px;
    margin: 0;
    font-size: 12.4px;
    line-height: 14.6px;
    text-align: justify;
    letter-spacing: 0.2px;
  }
  .upc-placeholder {
    position: absolute;
    left: 290px;
    top: 575px;
    width: 150px;
    height: 90px;
    background: var(--upc);
    border-radius: 8px;
  }
  .spine-title, .spine-author {
    position: absolute;
    left: 467px;
    writing-mode: vertical-rl;
    white-space: nowrap;
    transform: translateX(-50%);
  }
  .spine-title {
    top: 52px;
    font-family: "Kaushan Script", cursive;
    font-size: 22px;
  }
  .spine-author {
    top: 445px;
    font-family: "Cinzel", serif;
    font-size: 14px;
    letter-spacing: 0.5px;
  }
  .front-title {
    position: absolute;
    left: 495px;
    top: 82px;
    margin: 0;
    font-family: "Great Vibes", cursive;
    font-weight: 400;
    font-size: 64px;
    color: var(--title-red);
    white-space: nowrap;
  }
  .front-author {
    position: absolute;
    right: 22px;
    top: 500px;
    margin: 0;
    font-family: "Cinzel", serif;
    font-weight: 600;
    font-size: 34px;
    letter-spacing: 1px;
    white-space: nowrap;
  }
</style>
</head>
<body>
  <main class="book-cover">
    <div class="cover-photo" role="img" aria-label="Fotografía: silueta de una persona afligida sentada en un banco de madera, con luz blanca intensa detrás"></div>

    <section class="back-copy">
      <p>Por miles de años, se le ha dicho a la humanidad que el dolor es una parte necesaria de la vida, y que el profundo dolor después del fallecimiento de nuestros seres queridos es esperado y un proceso natural. Derek Fenwick dice enfáticamente que no, ¡no lo es! Puedes, y deberías estar emocionalmente estable y espiritualmente contento después de la muerte de un ser querido.</p>
      <p>La gente a veces pasa meses o años sumidos en el dolor paralizante, lo cual los aparta de muchos esfuerzos fructíferos. El dolor sabotea las vidas felices y productivas. Algunas veces la gente que trata con dolor extremo o pérdidas, se convierten en personas enojadas, abusan de las drogas y alcohol o incluso de quitan sus propias vidas. No debe ser de esta manera. La tristeza, cuando alguien se va de nuestras vidas, es normal. No es necesario el dolor intenso.</p>
      <p>Si crees que el dolor no es para ti – la paz emocional y la felicidad si lo son. Vence tu dolor ahora.</p>
      <p class="gap">La muerte, como parte de la vida, era una norma en la vida de cualquier persona normal. Ahora es raras veces discutida y solo cuando ocurre una emergencia. Senderos de Sauces es una franca discusión sobre la muerte y morir significa traer paz a los corazones de aquellas personas que están en duelo y esas personas que temen su propia muerte. No es insensible, oscuro y fuerte de leer pero es positivo, reconfortante y espiritualmente tranquilizador.</p>
    </section>

    <div class="author-band"></div>
    <div class="author-portrait" role="img" aria-label="Retrato del autor"></div>
    <p class="author-bio">Derek Fenwick se graduó de la Universidad Lakeshore Norte y desde entonces ha vivido en Nueva Jersey trabajando como editor y escritor en el mercado de masas, tecnologia y los campos de educación. Él es autor de otros tres libros de los que pueden encontrar más en DerekTfenwick.com</p>
    <div class="upc-placeholder"></div>

    <div class="spine-title">Senderos de Sauces</div>
    <div class="spine-author">Derek T. Fenwick</div>

    <h1 class="front-title">Senderos de Sauces</h1>
    <p class="front-author">Derek T. Fenwick</p>
  </main>
</body>
</html>
```